Global Expert Network Firm needs business card design

We need business card design for a new company based in Seoul, South Korea called 'Corwell Insight Partners'. We recruit industry experts covering all countries and connect our client and recruited expert by phone, face-to-face meetings and etc. We are a global expert network firm that is focused on delivering high-quality experts to our clients throughout the world. Our clients include multinational corporations, global consulting firms, private equity firms, venture capital firms, asset management companies.
We have made new logo and please find attachment.(Please use new logo)
Target Market(s)
Global Consulting Firms, Investment Firms, Private Equity Firms, Venture Capital Firms.
Industry/Entity Type
Recruitment
Contact Information for Business Card
We need two Languages (English and Korean Version).
The front is Korean and the back is English version.
[The back] [English]
Company Name: Corwell Insight Partners, Inc.
CEO Name: Daniel Park
Address: #507, Hanbit Bldg, 82 Maebongsan-ro, Dobong-gu, Seoul, 01327, Korea
Tel. +82 2 718 4052
Fax. +82 2 864 1097
Mobile. +82 10 7264 8815
Email: daniel@corwellip.com
Web: www.corwellip.com
[The front] [Korean] => Described in same order as English version.
회사명: 코웰인사이트파트너스(주)
대표이사: 박도현
주소: 서울시 도봉구 매봉산로 82 한빛빌딩 507호
Tel. 02 718 4052
Fax. 02 864 1097
Mobile. 010 7264 8815
Web: www.corwellip.com
Look and feel
Each slider illustrates characteristics of the customer's brand and the style your logo design should communicate.

```html
<!DOCTYPE html>
<html lang="ko">
<head>
<meta charset="utf-8">
<title>Corwell Insight Partners — Business Card</title>
<link rel="stylesheet" href="https://fonts.googleapis.com/css2?family=Marcellus&family=Karla:wght@400;500&family=Noto+Sans+KR:wght@400;500&display=swap">
<style>
  :root {
    --brand-navy: #364387;
    --card-white: #ffffff;
    --ink: #2b2b2b;
    --backdrop: #ece8e2;
    --rule-light: rgba(255,255,255,0.75);
  }
  html, body {
    margin: 0;
    padding: 0;
    width: 1200px;
    height: 1200px;
    overflow: hidden;
    background: var(--backdrop);
  }
  .canvas {
    position: relative;
    width: 1200px;
    height: 1200px;
  }
  .card {
    position: absolute;
    left: 150px;
    width: 900px;
    height: 500px;
    box-sizing: border-box;
    box-shadow: 0 6px 18px rgba(0,0,0,0.12);
  }
  .card--front { top: 70px; background: var(--card-white); color: var(--ink); }
  .card--back { top: 630px; background: var(--brand-navy); color: var(--card-white); }

  .brand {
    position: absolute;
    left: 56px;
    top: 60px;
    display: flex;
    align-items: center;
    gap: 16px;
    font-family: "Marcellus", serif;
    font-size: 30px;
    letter-spacing: 0.04em;
    white-space: nowrap;
  }
  .brand__square { width: 26px; height: 26px; display: block; }
  .card--front .brand { color: var(--brand-navy); }
  .card--front .brand__square { background: var(--brand-navy); }
  .card--back .brand { color: var(--card-white); }
  .card--back .brand__square { background: var(--card-white); }

  .person {
    position: absolute;
    right: 60px;
    text-align: right;
  }
  .card--front .person { top: 72px; }
  .card--back .person { top: 190px; }
  .person__name--ko {
    font-family: "Noto Sans KR", sans-serif;
    font-weight: 500;
    font-size: 34px;
    color: var(--brand-navy);
    letter-spacing: 0.05em;
  }
  .person__title--ko {
    font-family: "Noto Sans KR", sans-serif;
    font-size: 20px;
    color: var(--ink);
    letter-spacing: 0.08em;
    margin-top: 2px;
  }
  .person__name--en {
    font-family: "Marcellus", serif;
    font-size: 34px;
  }
  .person__title--en {
    font-family: "Karla", sans-serif;
    font-size: 20px;
    margin-top: 4px;
  }

  .company {
    position: absolute;
    left: 56px;
    right: 56px;
  }
  .card--front .company { top: 318px; }
  .card--back .company { top: 318px; }
  .company__name--ko {
    font-family: "Noto Sans KR", sans-serif;
    font-weight: 500;
    font-size: 32px;
    margin: 0 0 6px;
  }
  .company__name--en {
    font-family: "Marcellus", serif;
    font-size: 34px;
    font-weight: 400;
    margin: 0 0 6px;
  }
  .company__rule { display: block; width: 100%; height: 2px; margin-bottom: 12px; }
  .card--front .company__rule { background: var(--brand-navy); }
  .card--back .company__rule { background: var(--rule-light); }
  .card--front .company { top: 252px; }
  .card--front .company__rule { margin-bottom: 10px; order: -1; }

  .contact {
    font-family: "Karla", sans-serif;
    font-size: 21px;
    line-height: 28px;
    margin: 0;
    white-space: nowrap;
  }
  .contact--ko { font-family: "Noto Sans KR", "Karla", sans-serif; font-size: 20px; line-height: 32px; }
  .contact__sep { font-weight: 500; padding: 0 8px; }
  .card--front .contact__sep { color: var(--brand-navy); }
</style>
</head>
<body>
<main class="canvas">

  <section class="card card--front" lang="ko" aria-label="명함 앞면">
    <div class="brand">
      <span class="brand__square"></span>
      <span class="brand__name">Corwell Insight Partners</span>
    </div>
    <div class="person">
      <div class="person__name--ko">박도현</div>
      <div class="person__title--ko">대표이사</div>
    </div>
    <div class="company">
      <span class="company__rule"></span>
      <h2 class="company__name--ko">코웰인사이트파트너스(주)</h2>
      <p class="contact contact--ko">서울시 도봉구 매봉산로 82 한빛빌딩 507호<span class="contact__sep">|</span>Mobile. +82 10 7264 8815</p>
      <p class="contact contact--ko">Tel. +82 2 718 4052<span class="contact__sep">|</span>Fax. +82 2 864 1097</p>
      <p class="contact contact--ko">Email: daniel@corwellip.com<span class="contact__sep">|</span>Web: www.corwellip.com</p>
    </div>
  </section>

  <section class="card card--back" lang="en" aria-label="Business card back">
    <div class="brand">
      <span class="brand__square"></span>
      <span class="brand__name">Corwell Insight Partners</span>
    </div>
    <div class="person">
      <div class="person__name--en">Daniel Park</div>
      <div class="person__title--en">CEO</div>
    </div>
    <div class="company">
      <h2 class="company__name--en">Corwell Insight Partners, Inc.</h2>
      <span class="company__rule"></span>
      <p class="contact">#507, Hanbit Bldg, 82 Maebongsan-ro, Dobong-gu, Seoul, 01327, Korea</p>
      <p class="contact">Tel. +82 2 718 4052<span class="contact__sep">|</span>Fax. +82 2 864 1097<span class="contact__sep">|</span>Mobile. +82 10 7264 8815</p>
      <p class="contact">Email: daniel@corwellip.com<span class="contact__sep">|</span>Web: www.corwellip.com</p>
    </div>
  </section>

</main>
</body>
</html>
```